More Modern Look Required! Industry leading Property Management company needs a new website!

We are wanting to make our website more modern, as we find it is too cluttered, seems "old" and we want a new look. (www.tallowbrookrm.com)

We are wanting something fresh, clean and responsive, something that aligns with today's social media demands, something that allows our potential customers to immediately get a sense of the type of company we are.

Our current website was created on Wordpress and we will be keeping that core platform but wanting a new look and feel to it. The only thing we want to keep on the website is our "FOR RENT" page, although again we are open to having that look completely different as well (our programmers can adapt the functionality later)

Here is a synopsis of our branding statements:

CORE VALUES:
1. Passion
2. Innovation
3. Integrity (doing the right thing, even when it's difficult)
4. Empathy
5. Education

CORE FOCUS:
Our vision is to be the premier company for the delivery of all aspects of property management showing our passion for this industry, by innovating our service using cutting-edge technology, helping and educating investors to create aspirational and sustainable communities, adding value to their real estate assets, and working in partnership with all stakeholders including residents, showing empathy and integrity.

Brand Essence

When our customers experience our product or service, it brings forth an emotion of absolute trust that we have their best interests at heart

Brand Personality

We are a company that is passionate about our customers, our company and our vision to be leaders in the field of property management. We are visionaries that aren't afraid to use cutting edge technologies to improve our products and service.

Position or Value Proposition

To whom are we speaking?
- real estate investors, including first timers that are giving us their first starter home. They are not "big time" investors, and because they are giving us their first home (in contrast to an investor buying a rental property, often sight unseen) they are more emotionally tied to their property and will require a company that inspires trust and confidence.

What is our brand promise?
- we will do our best to serve our clients, both owners and tenants, to give them prompt communication, clear, concise answers to their questions, and look after their property quickly and competently.

Why is our product different than the competition and why should our customers care?
- Our management product is superior because we use a combination of technology and strict procedures to ensure each client's experience is consistent, each and every time.
Updates

Need extra days to review

Industry/Entity Type

Real Estate and Property Management

Number of Pages Required

5+ page

Requirements
Must have
• Must be compatible on Wordpress, our existing web platform. Please see our existing website at www.tallowbrookrm.com to familiarize yourself with our current site. Must incorporate For Rent section
Nice to have
• Built in reviews, contact us form, awards page including Fernleigh Patron Prizes (we just won again for Best Property Management Company, 8 years in a row)
Should not have
• Too many pages. Currently we feel there is too much information on each tab, and we can consolidate into about 5 or 6 tabs.

```html
<!DOCTYPE html>
<html lang="en">
<head>
<meta charset="utf-8">
<title>Tallowbrook Property Management</title>
<link rel="stylesheet" href="https://fonts.googleapis.com/css2?family=Libre+Baskerville:wght@400;700&family=Roboto:wght@400;500;700&display=swap">
<style>
:root{
  --blue:#1a8fd6;
  --blue-dark:#0f78bb;
  --ink:#1d1d1f;
  --muted:#555a60;
  --line:#c9ccd1;
  --soft:#f3f3f3;
  --dark:#0b0b0c;
  --footer:#262626;
  --white:#ffffff;
}
*{box-sizing:border-box;margin:0;padding:0}
html,body{width:1200px;height:4935px;overflow:hidden}
body{position:relative;font-family:"Roboto",Arial,sans-serif;color:var(--ink);background:var(--white)}
.abs{position:absolute}
.serif{font-family:"Libre Baskerville",Georgia,serif}
.ph{position:absolute}
.btn{position:absolute;display:flex;align-items:center;justify-content:space-between;padding:0 18px;font-size:12px;font-weight:700;border-radius:3px}
.btn .arr{width:20px;height:20px;border-radius:3px;display:flex;align-items:center;justify-content:center}
.btn-blue{background:var(--blue);color:var(--white)}
.btn-blue .arr{background:var(--white)}
.btn-white{background:var(--white);color:var(--ink)}
.btn-white .arr{background:var(--ink)}

/* hero */
.hero{position:absolute;left:0;top:0;width:1200px;height:608px;background:linear-gradient(160deg,#0e2a55 0%,#142a45 40%,#3a2c22 75%,#6b4a2e 100%)}
.brand{position:absolute;display:flex;align-items:center;gap:10px;color:var(--white);font-weight:700;letter-spacing:1px}
.brand .mark{width:26px;height:26px;border-radius:50%;background:var(--white)}
.nav{position:absolute;left:563px;top:40px;display:flex;gap:20px;color:var(--white);font-size:13px;font-weight:700}
.menu{position:absolute;left:1005px;top:40px;width:18px}
.menu i{display:block;height:2px;background:var(--white);margin-bottom:5px}
.hero h1{position:absolute;left:173px;top:198px;color:var(--white);font-size:42px;line-height:62px;font-weight:400;white-space:nowrap}
.hero p{position:absolute;left:173px;top:334px;width:600px;color:var(--white);font-size:12px;line-height:19px}
.hero-thumb{border:3px solid var(--white)}
.hero-bar{position:absolute;left:1024px;top:245px;width:2px;height:110px;background:var(--blue)}

/* why */
.why-title{position:absolute;left:660px;top:692px;width:370px;font-size:17px;line-height:27px;font-weight:500}
.why-text{position:absolute;left:660px;top:758px;width:370px;font-size:11.5px;line-height:18px;color:var(--muted)}
.why-text a{color:var(--blue);text-decoration:none}
.why-text p{margin-bottom:12px}
.badge{position:absolute}

/* video */
.caption{position:absolute;left:173px;top:1466px;width:560px;font-size:24px;line-height:37px}
.play{position:absolute;left:440px;top:1285px;width:70px;height:70px;border:3px solid var(--white);border-radius:50%;display:flex;align-items:center;justify-content:center}

/* services */
.svc-bg{position:absolute;left:215px;top:1600px;width:985px;height:378px;background:var(--soft)}
.sec-title{font-size:26px;font-weight:700}
.svc-text{position:absolute;left:173px;top:1766px;width:335px;font-size:11.5px;line-height:18px;color:var(--muted)}
.svc-card-label{position:absolute;color:var(--white);font-size:12px;text-align:center;width:211px}

/* rent */
.rent{position:absolute;left:0;top:1994px;width:1200px;height:396px;background:var(--dark)}

/* stats */
.stat{position:absolute;width:160px;text-align:center}
.stat .num{font-size:50px;font-weight:700;color:#e8e8e8;line-height:56px}
.stat .lbl{position:absolute;left:0;top:14px;width:160px;font-family:"Libre Baskerville",Georgia,serif;font-size:13px;font-weight:700}

/* tabs */
.tabs{position:absolute;left:0;top:3172px;width:1200px;display:flex;justify-content:center;gap:30px;font-size:17px}
.tabs .on{border-bottom:2px solid var(--blue);padding-bottom:6px}

/* reviews */
.reviews{position:absolute;left:0;top:3621px;width:1200px;height:376px;background:#f7f7f7}
.avatar{position:absolute;width:80px;height:80px;border-radius:50%}
.stars{position:absolute;left:531px;top:3762px;color:#f5b301;font-size:14px;letter-spacing:1px}
.quote{position:absolute;left:531px;top:3784px;width:500px;font-size:12px;line-height:19px;color:#333}
.circ{position:absolute;width:22px;height:22px;border:1px solid #777;border-radius:50%}

/* contact */
.field{position:absolute;border-bottom:1px solid var(--line);font-size:12px;color:#666;padding-bottom:10px}

/* info band */
.info{position:absolute;left:0;top:4549px;width:1200px;height:151px;background:var(--blue)}
.info-item{position:absolute;display:flex;align-items:center;gap:14px;color:var(--white)}
.info-item .ring{width:60px;height:60px;border:2px solid var(--white);border-radius:50%;display:flex;align-items:center;justify-content:center}
.info-item small{display:block;font-size:14px;margin-bottom:8px}
.info-item b{font-size:15px}

/* footer */
.footer{position:absolute;left:0;top:4700px;width:1200px;height:235px;background:var(--footer)}
.fnav{position:absolute;left:0;top:145px;width:1200px;display:flex;justify-content:center;gap:28px;font-size:12.5px;color:var(--white)}
.fnav .on{color:var(--blue)}
.copy{position:absolute;left:173px;top:198px;font-size:11px;color:#d0d0d0}
.social{position:absolute;top:190px;width:24px;height:24px;background:var(--white);border-radius:4px}
</style>
</head>
<body>

<section class="hero">
  <div class="brand" style="left:173px;top:36px;font-size:14px"><span class="mark"></span>TALLOWBROOK</div>
  <nav class="nav"><span>HOME</span><span>SERVICES</span><span>PRICING</span><span>HOME WATCH</span><span>CONTACT US</span></nav>
  <div class="menu"><i></i><i></i><i style="width:12px"></i></div>
  <h1 class="serif">Lorem Ipsum has been the<br>industry's standard</h1>
  <p>It is a long established fact that a reader will be distracted by the readable content of a page when looking at its layout.sometimes on purpose (injected humour and the like).</p>
  <div class="btn btn-blue" style="left:173px;top:404px;width:210px;height:41px">Existing Tenant Login<span class="arr"><svg width="10" height="10" viewBox="0 0 10 10"><path d="M1 5h7M5 2l3 3-3 3" stroke="#1a8fd6" fill="none" stroke-width="1.5"/></svg></span></div>
  <div class="btn btn-white" style="left:403px;top:404px;width:210px;height:41px">Exixting Owner Login<span class="arr"><svg width="10" height="10" viewBox="0 0 10 10"><path d="M1 5h7M5 2l3 3-3 3" stroke="#fff" fill="none" stroke-width="1.5"/></svg></span></div>
  <div class="ph hero-thumb" role="img" aria-label="Modern house at dusk" style="left:815px;top:197px;width:182px;height:115px;background:linear-gradient(180deg,#4a8fd0,#7fb06a)"></div>
  <div class="ph hero-thumb" role="img" aria-label="Modern house under a pink sunset sky" style="left:815px;top:332px;width:182px;height:115px;background:linear-gradient(180deg,#6a5bb8,#d88aa0 55%,#3d4a3a)"></div>
  <div class="hero-bar"></div>
</section>

<div class="ph" role="img" aria-label="Two-storey suburban home at sunset" style="left:173px;top:667px;width:286px;height:162px;background:linear-gradient(180deg,#6a7fb8,#b38a8a 55%,#5f6a5a);border:3px solid #fff;box-shadow:0 0 0 1px #ddd"></div>
<div class="ph" role="img" aria-label="Modern glass house facade" style="left:467px;top:713px;width:112px;height:116px;background:linear-gradient(180deg,#c9d7e6,#4c5560)"></div>
<div class="ph" role="img" aria-label="Palm trees beside a resort at sunset" style="left:226px;top:783px;width:156px;height:287px;background:linear-gradient(180deg,#d69a7a,#8a5a4a 60%,#3a3030)"></div>
<div class="ph" role="img" aria-label="Contemporary house with orange and white walls" style="left:390px;top:783px;width:239px;height:214px;background:linear-gradient(180deg,#cfe0ee,#9a5a3a 50%,#5a7a4a)"></div>
<h2 class="why-title">Why Choose Tallowbrook As Your Property Management Company</h2>
<div class="why-text">
  <p>Tallowbrook Property Management has been recognized and voted multiple times as The Best <a>Winnipeg Property Management</a> Company by Fernleigh Patron Prizes. We are intently focussed on serving both owners and tenants and are dedicated to a culture of superior customer service.</p>
  <p>Whether you own one investment property or ten, the partnership process with Tallowbrook Property Management is easy, efficient and rewarding.</p>
</div>
<div class="badge" style="left:660px;top:935px;width:170px;height:48px;background:#d9dde6;border-radius:3px"></div>
<div class="badge" style="left:862px;top:935px;width:48px;height:48px;background:#2b5aa8;border-radius:50%"></div>
<div class="badge" style="left:940px;top:935px;width:34px;height:48px;background:#b5451f;border-radius:4px"></div>
<div class="btn btn-blue" style="left:660px;top:1004px;width:210px;height:44px">Know More About Us<span class="arr"><svg width="10" height="10" viewBox="0 0 10 10"><path d="M1 5h7M5 2l3 3-3 3" stroke="#1a8fd6" fill="none" stroke-width="1.5"/></svg></span></div>

<div class="ph" role="img" aria-label="Rooftop terrace overlooking trees" style="left:173px;top:1196px;width:602px;height:248px;background:linear-gradient(180deg,#dfe6e2,#6f8a5a 45%,#5a4a3a)"></div>
<div class="play"><svg width="22" height="26" viewBox="0 0 22 26"><path d="M2 1l19 12L2 25z" fill="#fff"/></svg></div>
<div class="ph" role="img" aria-label="Line drawing of a modern building" style="left:775px;top:1215px;width:252px;height:290px;background:linear-gradient(180deg,#f3f3f3,#fafafa)"></div>
<p class="caption">Is managing a property easy? Watch the video to find out!|</p>

<div class="svc-bg"></div>
<h2 class="abs serif sec-title" style="left:173px;top:1712px">Our Services</h2>
<p class="svc-text">Tallowbrook Property Management in Winnipeg offers some of the most premium services available for investors and tenants.</p>
<div class="btn btn-blue" style="left:173px;top:1840px;width:168px;height:42px">View Services<span class="arr"><svg width="10" height="10" viewBox="0 0 10 10"><path d="M1 5h7M5 2l3 3-3 3" stroke="#1a8fd6" fill="none" stroke-width="1.5"/></svg></span></div>
<div class="ph" role="img" aria-label="Dark interior photo behind service card" style="left:525px;top:1664px;width:211px;height:266px;background:linear-gradient(180deg,#2a2c30,#121314)"></div>
<svg class="abs" style="left:610px;top:1738px" width="42" height="40" viewBox="0 0 42 40"><path d="M4 20L21 5l17 15M9 16v20h24V16M17 36V25h8v11" stroke="#fff" fill="none" stroke-width="2"/></svg>
<div class="svc-card-label" style="left:525px;top:1800px">Property Management</div>
<div class="svc-card-label" style="left:525px;top:1838px;font-weight:700;text-decoration:underline;font-size:11px">Learn More</div>
<div class="ph" role="img" aria-label="Rooftop lounge with city view" style="left:757px;top:1664px;width:211px;height:266px;background:linear-gradient(180deg,#b8c6d6,#7a8a9a 50%,#4f8a3a)"></div>
<div class="ph" role="img" aria-label="Villa with pool at dusk" style="left:987px;top:1664px;width:213px;height:266px;background:linear-gradient(180deg,#2f5ab0,#c9875a 60%,#6a3a2a)"></div>

<section class="rent">
  <h2 class="abs serif sec-title" style="left:0;top:60px;width:1200px;text-align:center;color:#fff;font-size:24px">Our Rent</h2>
  <div class="ph" role="img" aria-label="Covered patio" style="left:173px;top:128px;width:153px;height:207px;background:linear-gradient(180deg,#3a3a3a,#1f1f1f)"></div>
  <div class="abs" style="left:215px;top:222px;color:#fff;font-size:13px;text-decoration:underline">View More</div>
  <div class="ph" role="img" aria-label="Modern house with pool" style="left:347px;top:162px;width:155px;height:140px;background:linear-gradient(180deg,#8fb3d6,#3a6a7a 60%,#2a8ab0)"></div>
  <div class="ph" role="img" aria-label="Bright dining room" style="left:521px;top:128px;width:156px;height:207px;background:linear-gradient(180deg,#f0e6d6,#c9a070)"></div>
  <div class="ph" role="img" aria-label="House under blue sky" style="left:696px;top:162px;width:155px;height:140px;background:linear-gradient(180deg,#2a5aa8,#5a7a8a 60%,#3a5a3a)"></div>
  <div class="ph" role="img" aria-label="Lit terrace at sunset" style="left:872px;top:128px;width:155px;height:207px;background:linear-gradient(180deg,#e09a5a,#5a4a5a 55%,#2a2020)"></div>
</section>

<h2 class="abs serif sec-title" style="left:0;top:2452px;width:1200px;text-align:center;font-size:25px">Currently Under Management</h2>
<svg class="abs" style="left:315px;top:2520px" width="60" height="62" viewBox="0 0 60 62"><path d="M20 60V28L40 10l16 14v36zM4 60V40l14-12" fill="#1a8fd6"/><rect x="36" y="30" width="8" height="8" fill="#fff"/></svg>
<svg class="abs" style="left:570px;top:2522px" width="62" height="60" viewBox="0 0 62 60"><path d="M4 28L31 4l27 24M12 22v36h38V22" stroke="#1a8fd6" stroke-width="5" fill="none"/><circle cx="24" cy="36" r="5" fill="#1a8fd6"/><circle cx="38" cy="36" r="5" fill="#1a8fd6"/><rect x="18" y="42" width="26" height="16" fill="#1a8fd6"/></svg>
<svg class="abs" style="left:828px;top:2520px" width="54" height="62" viewBox="0 0 54 62"><circle cx="14" cy="8" r="6" fill="#1a8fd6"/><circle cx="40" cy="8" r="6" fill="#1a8fd6"/><path d="M6 18h16v22h-4v20h-8V40H6zM32 18h16v22h-4v20h-8V40h-4z" fill="#1a8fd6"/></svg>
<div class="stat" style="left:265px;top:2598px"><div class="num">477</div><div class="lbl">Properties</div></div>
<div class="stat" style="left:520px;top:2598px"><div class="num">542</div><div class="lbl">Units</div></div>
<div class="stat" style="left:775px;top:2598px"><div class="num">377</div><div class="lbl">Investors</div></div>
<div class="ph" role="img" aria-label="Large modern home lit at dusk" style="left:220px;top:2674px;width:807px;height:316px;background:linear-gradient(180deg,#4f5a6e,#8a8f98 40%,#3a2f28 75%,#3a5a2a)"></div>
<div class="abs" style="left:173px;top:2929px;width:383px;height:61px;background:#fff;color:var(--blue);font-size:14px;font-weight:500;padding:27px 0 0 19px">Click HERE to use our free Market Rent Calculator</div>

<h2 class="abs serif sec-title" style="left:0;top:3112px;width:1200px;text-align:center;font-size:25px">Properties Managed by Tallowbrook</h2>
<div class="tabs"><span class="on">All Properties</span><span>Available Properties</span></div>
<div class="ph" role="img" aria-label="Map of managed property locations" style="left:0;top:3234px;width:1200px;height:387px;background:linear-gradient(135deg,#b9cfa0,#9dbb86 50%,#c7d4a8)"></div>

<section class="reviews">
  <h2 class="abs serif sec-title" style="left:0;top:64px;width:1200px;text-align:center;font-size:25px">See what our clients are saying in our latest Vantly Reviews</h2>
  <div class="avatar" role="img" aria-label="Reviewer portrait" style="left:184px;top:127px;background:#5a4a44"></div>
  <div class="avatar" role="img" aria-label="Reviewer portrait" style="left:293px;top:127px;background:#c9a48e"></div>
  <div class="avatar" role="img" aria-label="Reviewer portrait" style="left:393px;top:127px;background:#f0a020"></div>
  <div class="abs" style="left:172px;top:226px;width:105px;text-align:center;color:var(--blue);font-size:12px;font-weight:500">MARA DELLOW</div>
  <div class="abs" style="left:172px;top:244px;width:105px;text-align:center;font-size:11px;color:#333">3/11/2022</div>
  <div class="circ" style="left:572px;top:300px"></div>
  <div class="circ" style="left:605px;top:300px"></div>
</section>
<div class="stars">★★★★★</div>
<p class="quote">The management are very very helpful. They respond quick to any request you may have, email is replied within hours if not minutes, the repair team are very professionals as well. They are really really great company to rent from. The best decision I have made.</p>

<h2 class="abs serif sec-title" style="left:546px;top:4062px;width:481px;text-align:center;font-size:25px">Contact Us</h2>
<div class="ph" role="img" aria-label="Phone showing a route on a city map" style="left:192px;top:4150px;width:326px;height:287px;background:radial-gradient(ellipse at center,#e3eef8 0%,#f5f8fb 60%,#fff 100%)"></div>
<div class="field" style="left:546px;top:4152px;width:232px">Name</div>
<div class="field" style="left:790px;top:4152px;width:237px">Phone</div>
<div class="field" style="left:546px;top:4219px;width:481px">email</div>
<div class="field" style="left:546px;top:4287px;width:481px">What are you?<svg class="abs" style="right:14px;top:2px" width="14" height="8" viewBox="0 0 14 8"><path d="M1 1l6 6 6-6" stroke="#333" fill="none" stroke-width="1.5"/></svg></div>
<div class="field" style="left:546px;top:4356px;width:481px;height:60px">Questions or Services interested in</div>
<div class="btn btn-blue" style="left:723px;top:4447px;width:124px;height:43px">Submit<span class="arr"><svg width="10" height="10" viewBox="0 0 10 10"><path d="M1 5h7M5 2l3 3-3 3" stroke="#1a8fd6" fill="none" stroke-width="1.5"/></svg></span></div>

<section class="info">
  <div class="info-item" style="left:173px;top:45px"><span class="ring"><svg width="28" height="28" viewBox="0 0 24 24"><path d="M6 2l4 4-2 3c1 3 3 5 6 6l3-2 4 4-3 4C9 21 3 15 2 5z" stroke="#fff" fill="none" stroke-width="1.6"/></svg></span><div><small>Phone Number</small><b>204-555-0148</b></div></div>
  <div class="info-item" style="left:470px;top:45px"><span class="ring"><svg width="28" height="28" viewBox="0 0 24 24"><path d="M6 2l4 4-2 3c1 3 3 5 6 6l3-2 4 4-3 4C9 21 3 15 2 5z" stroke="#fff" fill="none" stroke-width="1.6"/></svg></span><div><small>Toll Free Number</small><b>1-800-555-0192</b></div></div>
  <div class="info-item" style="left:782px;top:45px"><span class="ring"><svg width="30" height="22" viewBox="0 0 30 22"><rect x="1" y="1" width="28" height="20" rx="2" stroke="#fff" fill="none" stroke-width="1.6"/><path d="M1 2l14 11L29 2" stroke="#fff" fill="none" stroke-width="1.6"/></svg></span><div><small style="font-size:12px">Our Email Address</small><b>info@tallowbrookrm.com</b></div></div>
</section>

<footer class="footer">
  <div class="brand" style="left:0;width:1200px;justify-content:center;top:62px;font-size:26px;letter-spacing:3px"><span class="mark" style="width:36px;height:36px;background:var(--blue)"></span>TALLOWBROOK</div>
  <nav class="fnav"><span class="on">HOME</span><span>SERVICES</span><span>RENTALS</span><span>PRICING</span><span>FAQS</span><span>ABOUT US</span><span>CONTACT US</span><span>CONTRACTORS</span></nav>
  <div class="copy">© 2019 Tallowbrook Property Management. All right reserved.</div>
  <div class="social" style="left:871px"></div>
  <div class="social" style="left:914px"></div>
  <div class="social" style="left:957px"></div>
  <div class="social" style="left:1001px"></div>
</footer>

</body>
</html>
```